High Tech Real Estate Startup needs a business card

We are developing an innovative real estate marketing product based around advanced search and virtual reality.

We talk to people, we need business cards.

Target Market(s)

The target market is technology professionals and realtors.

Contact Information for Business Card

The information to be included will include

Name
Title
Phone Number
E-mail Address
www.quelzo.com

It should use simple iconography for each one of those fields.

Font styles to use
Other font styles liked:
• Co, Jubilat, Avenir

Colors

Designer to choose colors to be used in the design.

Requirements
Must have
• Clean aesthetic,
• Good use of negative space.
• It should use our company logo, shown in the attached file. It is able to use the negative of that logo (coloured font and white background) and I have attached other acceptable accent colours in a swatch file.
Should not have
• Should not be too busy
• No extraneous text (slogans, tag lines etc)

```html
<!DOCTYPE html>
<html lang="en">
<head>
<meta charset="utf-8">
<title>Quelzo business card</title>
<link rel="stylesheet" href="https://fonts.googleapis.com/css2?family=Mulish:wght@400;600;700&display=swap">
<style>
  :root {
    --teal: #0fb1b4;
    --teal-deep: #05a5a9;
    --white: #f7f7f7;
    --paper: #f1f1f1;
    --ink: #4a4a4a;
    --backdrop: #2e2e30;
  }
  * { box-sizing: border-box; margin: 0; padding: 0; }
  html, body { width: 1200px; height: 890px; overflow: hidden; }
  body {
    background: var(--backdrop);
    font-family: "Mulish", "Avenir", sans-serif;
    position: relative;
  }
  .card {
    position: absolute;
    top: 165px;
    width: 320px;
    height: 560px;
    border-radius: 2px;
    box-shadow: 0 10px 30px rgba(0,0,0,.35);
  }
  .card--front { left: 230px; background: var(--paper); }
  .card--back  { left: 650px; background: var(--teal); }

  .holder { position: absolute; top: 44px; width: 100%; text-align: center; }
  .holder__name {
    color: var(--teal); font-weight: 700; font-size: 15px; letter-spacing: .02em;
  }
  .holder__title { color: var(--ink); font-size: 11px; margin-top: 2px; }

  .logo-block {
    position: absolute; left: 50%; transform: translateX(-50%);
    display: flex; align-items: center; justify-content: center;
  }
  .card--front .logo-block {
    top: 140px; width: 240px; height: 166px; background: var(--teal);
  }
  .card--back .logo-block {
    top: 190px; width: 240px; height: 190px; background: var(--white);
  }
  .logo-name {
    font-weight: 600; font-size: 30px; letter-spacing: .06em;
  }
  .card--front .logo-name { color: var(--white); }
  .card--back .logo-name { color: var(--teal); }

  .contacts {
    position: absolute; top: 402px; left: 0; width: 100%;
    list-style: none; display: flex; flex-direction: column; align-items: center; gap: 3px;
  }
  .contacts li {
    display: flex; align-items: center; gap: 10px;
    color: var(--ink); font-size: 15px; width: 190px;
  }
  .contacts svg { width: 14px; height: 14px; flex: none; }

  .site {
    position: absolute; top: 404px; width: 100%; text-align: center;
    color: var(--white); font-size: 14px; letter-spacing: .42em;
  }
</style>
</head>
<body>
  <section class="card card--front">
    <header class="holder">
      <p class="holder__name">JORDAN PELLEY</p>
      <p class="holder__title">General Manager</p>
    </header>
    <div class="logo-block"><span class="logo-name">QUELZO</span></div>
    <ul class="contacts">
      <li>
        <svg viewBox="0 0 16 16" aria-hidden="true"><path fill="#0fb1b4" d="M4 1.5l2.2 3-1.3 1.6c.8 1.8 2.2 3.2 4 4l1.6-1.3 3 2.2-1.2 2.6C7.5 14 2 8.5 1.4 2.7z"/></svg>
        <span>616-555-0187</span>
      </li>
      <li>
        <svg viewBox="0 0 16 16" aria-hidden="true"><rect x="1" y="3.5" width="14" height="9" fill="#0fb1b4"/><path d="M1.5 4l6.5 5 6.5-5" fill="none" stroke="#f1f1f1" stroke-width="1.2"/></svg>
        <span>info@quelzo.com</span>
      </li>
      <li>
        <svg viewBox="0 0 16 16" aria-hidden="true"><g fill="none" stroke="#0fb1b4" stroke-width="1.3"><circle cx="8" cy="8" r="6.5"/><ellipse cx="8" cy="8" rx="3" ry="6.5"/><path d="M1.5 8h13M2.5 5h11M2.5 11h11"/></g></svg>
        <span>www.quelzo.com</span>
      </li>
    </ul>
  </section>

  <section class="card card--back">
    <div class="logo-block"><span class="logo-name">QUELZO</span></div>
    <p class="site">WWW.QUELZO.COM</p>
  </section>
</body>
</html>
```